KV MOTORS BANNER/SIGN DESIGN

Design a banner sign for outdoor use for KV MOTORS - a premium pre owned vehicle sales center. The size must be 36 feet in width
and 3 feet in height.

Information required: logo (attached)
-PREMIUM PRE-OWEND VEHICLE SALES
- 403.555.0172

perhaps in smaller font: BUY-SELL-TRADE

prefer white background but could possibly do red matching the logo

```html
<!DOCTYPE html>
<html lang="en">
<head>
<meta charset="utf-8">
<title>KV Motors Banner</title>
<link href="https://fonts.googleapis.com/css2?family=Anton&display=swap" rel="stylesheet">
<style>
  :root {
    --backdrop: #808080;
    --banner-white: #ffffff;
    --ink-black: #050505;
    --brand-red: #e30613;
  }
  * { margin: 0; padding: 0; box-sizing: border-box; }
  html, body {
    width: 1200px;
    height: 600px;
    overflow: hidden;
    background: var(--backdrop);
  }
  .banner {
    position: absolute;
    left: 77px;
    top: 256px;
    width: 1046px;
    height: 88px;
    display: flex;
    font-family: "Anton", "Impact", sans-serif;
  }
  .banner-main {
    flex: 1;
    background: var(--banner-white);
    display: flex;
    align-items: center;
    padding-left: 18px;
  }
  .brand {
    display: flex;
    align-items: center;
    gap: 10px;
    margin-right: 16px;
  }
  .brand-dot {
    width: 38px;
    height: 38px;
    border-radius: 50%;
    background: var(--brand-red);
  }
  .brand-name {
    font-size: 24px;
    color: var(--ink-black);
    letter-spacing: 1px;
    white-space: nowrap;
  }
  .headline {
    font-size: 50px;
    line-height: 1;
    white-space: nowrap;
    letter-spacing: -0.3px;
    color: var(--ink-black);
    transform: scaleX(0.92);
    transform-origin: left center;
  }
  .headline-accent { color: var(--brand-red); }
  .banner-contact {
    width: 209px;
    background: var(--ink-black);
    display: flex;
    flex-direction: column;
    align-items: center;
    justify-content: center;
    gap: 6px;
  }
  .services {
    color: var(--banner-white);
    font-size: 25px;
    line-height: 1;
    letter-spacing: -0.2px;
  }
  .phone {
    background: var(--brand-red);
    color: var(--banner-white);
    font-size: 22px;
    line-height: 1;
    width: 164px;
    height: 29px;
    border-radius: 15px;
    display: flex;
    align-items: center;
    justify-content: center;
  }
</style>
</head>
<body>
  <div class="banner">
    <div class="banner-main">
      <div class="brand">
        <span class="brand-dot"></span>
        <span class="brand-name">KV MOTORS</span>
      </div>
      <h1 class="headline">PREMIUM PRE-OWEND <span class="headline-accent">VEHICLE SALES</span></h1>
    </div>
    <div class="banner-contact">
      <p class="services">BUY-SELL-TRADE</p>
      <p class="phone">403.555.0172</p>
    </div>
  </div>
</body>
</html>
```